Design of a Job Advert to inspire people to join our movement

I am looking for a very cool ad to be designed to attract staff to a company. the ad needs to The key objective of this advertisement is to attract Co-creators to join our movement and get an equity share in the platform.

We need to be daring and creative and really get the attention of quality capable resources that can help us to co-create our platform. Which aligns directly with the structure of the company.

The advertisement needs to be very exciting and eye catching. There are key messages that we need to be shown very clearly and needs to pop off the page.

I have attached the ad with all the text changes also I have attached a document that shows the key messages.

I have also included some images from the app for you to use if you feel they will add value.

Can you design an ad that would inspire you personally to be curious to investigate what it is all about.

Something very visually inspiring that is easy to read the key messages.
I will leave it your creative licence.

Thanks and really look forward to seeing the next iteration

Regards Maren

Target Market(s)

Poeple who work for oVax

Requirements
Must have
• Very catching and emotive to move people to understand our movement and join us

```html
<!DOCTYPE html>
<html lang="en">
<head>
<meta charset="utf-8">
<title>Are You oVax? – Co-creator Advert</title>
<link rel="stylesheet" href="https://fonts.googleapis.com/css2?family=Anton&family=Oswald:wght@300;400;500&display=swap">
<style>
  :root {
    --page-bg: #ffffff;
    --brand-blue: #47a3d3;
    --heading-blue: #1f7db3;
    --deep-blue: #176a9a;
    --ink: #1e1e1e;
    --rule: #6f8796;
    --map-tint: #edf4fa;
    --phone-frame: #f3f3f3;
    --phone-edge: #d9d9d9;
  }
  * { box-sizing: border-box; margin: 0; padding: 0; }
  html, body {
    width: 922px; height: 1200px; overflow: hidden;
    background: var(--page-bg);
  }
  .canvas { position: relative; width: 922px; height: 1200px; }
  .poster {
    position: absolute; left: 37px; top: 0;
    width: 649px; height: 918px;
    transform: scale(1.3072); transform-origin: top left;
    background: var(--page-bg);
    font-family: "Oswald", "Arial Narrow", sans-serif;
    color: var(--ink);
  }
  .world-map {
    position: absolute; left: 0; top: 120px; width: 580px; height: 750px;
    border-radius: 50%;
    background: radial-gradient(ellipse at 55% 45%, var(--map-tint) 0%, var(--map-tint) 55%, rgba(237,244,250,0) 72%);
  }
  .intro-tagline {
    position: absolute; right: calc(649px - 295px); top: 66px; width: 200px;
    text-align: right; color: var(--heading-blue);
    font-weight: 500; font-size: 15.5px; line-height: 24px;
  }
  .intro-copy {
    position: absolute; left: 321px; top: 66px; width: 275px;
    font-weight: 300; font-size: 12.6px; line-height: 19.5px;
    text-align: justify;
  }
  .rule { position: absolute; left: 148px; width: 444px; height: 1px; background: var(--rule); }
  .rule--top { top: 164px; }
  .rule--bottom { top: 406px; }
  .headline { position: absolute; left: 146px; top: 176px; }
  .question { position: absolute; left: 0; top: 0; width: 460px; height: 200px; }
  .phone {
    position: absolute; border-radius: 14px; background: var(--phone-frame);
    border: 1px solid var(--phone-edge);
    box-shadow: 0 6px 10px rgba(0,0,0,0.12); padding: 5px;
  }
  .phone__screen { width: 100%; height: 100%; border-radius: 10px; }
  .phone--left { left: 198px; top: 423px; width: 103px; height: 215px; }
  .phone--center { left: 303px; top: 393px; width: 138px; height: 275px; z-index: 2; }
  .phone--right { left: 443px; top: 425px; width: 104px; height: 213px; }
  .screen--profile { background: linear-gradient(180deg, #c9c2b6 0%, #d69a5e 55%, #6b4e3a 100%); }
  .screen--powers { background: linear-gradient(180deg, #8c8c8c 0%, #3a3a3a 40%, #1b1b1b 100%); }
  .screen--video { background: linear-gradient(180deg, #c9b59b 0%, #7aa3c9 60%, #4f7ea8 100%); }
  .community-title {
    position: absolute; right: calc(649px - 284px); top: 688px; width: 200px;
    text-align: right; color: var(--heading-blue); text-transform: uppercase;
    font-weight: 500; font-size: 16.5px; line-height: 23px;
  }
  .community-list {
    position: absolute; left: 309px; top: 689px; list-style: none;
    font-weight: 300; font-size: 12px; line-height: 19.8px;
  }
  .call-to-action {
    position: absolute; left: 148px; top: 843px; width: 446px;
    text-align: right; color: var(--heading-blue); text-transform: uppercase;
    font-weight: 500; font-size: 16.5px; letter-spacing: 0.2px; white-space: nowrap;
  }
</style>
</head>
<body>
<main class="canvas">
  <article class="poster">
    <div class="world-map" role="img" aria-label="Faint pale-blue world map in the background"></div>

    <h2 class="intro-tagline">The oVax platform that is community built, managed and owned</h2>
    <p class="intro-copy">The world has changed forever, disruption is inevitable and we are looking for the best talent to partner with us through our unique equity participation program</p>

    <div class="rule rule--top"></div>

    <h1 class="headline">
      <svg class="question" viewBox="0 0 460 200" aria-label="Are you oVax?">
        <text x="3" y="78" font-family="Anton, sans-serif" font-size="55" fill="var(--brand-blue)" textLength="76" lengthAdjust="spacingAndGlyphs">ARE</text>
        <text x="3" y="130" font-family="Anton, sans-serif" font-size="55" fill="var(--brand-blue)" textLength="76" lengthAdjust="spacingAndGlyphs">YOU</text>
        <text x="98" y="192" font-family="Anton, sans-serif" font-size="248" fill="var(--brand-blue)" textLength="340" lengthAdjust="spacingAndGlyphs">oVax</text>
        <text x="432" y="192" font-family="Anton, sans-serif" font-size="32" fill="var(--deep-blue)">?</text>
      </svg>
    </h1>

    <div class="rule rule--bottom"></div>

    <div class="phone phone--left"><div class="phone__screen screen--profile" role="img" aria-label="App screen: member profile video with a short problem-solving caption"></div></div>
    <div class="phone phone--center"><div class="phone__screen screen--powers" role="img" aria-label="App screen: grid of superpower skill icons to unlock"></div></div>
    <div class="phone phone--right"><div class="phone__screen screen--video" role="img" aria-label="App screen: member recording a video with a record button"></div></div>

    <h3 class="community-title">The Novaair community where:</h3>
    <ul class="community-list">
      <li>User are paid for their data</li>
      <li>Platform 100% owned by the users</li>
      <li>Democratised Internet of the future is built</li>
      <li>Decentralised Technologies are core</li>
      <li>Global Equality and Fairness and consent are a right</li>
      <li>Individuals excel and are empowered by the community</li>
      <li>Marketing and Advertising is re-imagined</li>
    </ul>

    <p class="call-to-action">Join our mission in delivering the future of the internet!</p>
  </article>
</main>
</body>
</html>
```